EdTech Pellino

We am looking for complete redesign of our Mobile learning app and looking for a simple and best UI/UX design and ICON for our App. I have mentioned our app link below .
We sell Mobile app for students who prepares for Medical exams Educational apps.

We like a simple design , you can refer these apps
https://apps.storefrontdemo.test/us/app/vorlix-learn-languages-spanish-french-more/id504918273?mt=8

https://market.droidshelf.test/store/apps/details?id=fi.kx.android.tarvella&hl=en

our app:
IOS APP
https://apps.storefrontdemo.test/us/app/qorm-brevatel-rn-exam-prep-2017-edition/id1739025418?mt=8
Android
https://market.droidshelf.test/store/apps/details?id=com.pellinoworks.elearning.android.brevatelrn&hl=en

Target Market(s)

Our target audience are Medical student , age of 20 to 40

Industry/Entity Type

Medical

Font styles to use
Sans Serif

Colors
33a6d7
72c9bd
faa54b
f68d4d
3176b5

Requirements
Must have
• Icon and UX
Nice to have
• a better design for our test history as well

```html
<!DOCTYPE html>
<html lang="en">
<head>
<meta charset="utf-8">
<title>EdTech Pellino – Settings Menu</title>
<link href="https://fonts.googleapis.com/css2?family=Montserrat:wght@400;500&display=swap" rel="stylesheet">
<style>
  :root {
    --page-bg: #19222b;
    --screen-bg: #c9cacb;
    --card-bg: #ebebec;
    --divider: #cfcfd1;
    --ink: #1d1f22;
    --blob-purple: #6a45c8;
    --blob-green: #2f9a5c;
    --blob-teal: #2a8f7e;
    --blob-brown: #7a6456;
    --blob-pink: #d68aa8;
    --blob-grey: #a9aaab;
  }
  * { box-sizing: border-box; margin: 0; padding: 0; }
  html, body {
    width: 1200px; height: 1200px; overflow: hidden;
    background: var(--page-bg);
    font-family: "Montserrat", sans-serif;
  }
  .screen {
    position: absolute; left: 290px; top: 40px;
    width: 620px; height: 1120px;
    background: var(--screen-bg);
    overflow: hidden;
    border-radius: 6px;
  }
  .backdrop { position: absolute; inset: 0; }
  .blob { position: absolute; border-radius: 50%; filter: blur(40px); }
  .blob--grey-top { left: 160px; top: 90px; width: 220px; height: 130px; background: var(--blob-grey); }
  .blob--grey-mid { left: 40px; top: 420px; width: 260px; height: 200px; background: var(--blob-grey); }
  .blob--brown { left: 40px; top: 740px; width: 220px; height: 160px; background: var(--blob-brown); }
  .blob--pink { left: 500px; top: 300px; width: 160px; height: 160px; background: var(--blob-pink); opacity: .7; }
  .blob--purple { left: 380px; top: 640px; width: 300px; height: 260px; background: var(--blob-purple); }
  .blob--green { left: 140px; top: 900px; width: 340px; height: 260px;
    background: radial-gradient(circle, var(--blob-teal), var(--blob-green)); }

  .settings-button {
    position: absolute; right: 28px; top: 30px;
    width: 84px; height: 84px; border-radius: 50%;
    background: var(--card-bg);
    display: flex; align-items: center; justify-content: center;
  }
  .menu-card {
    position: absolute; left: 30px; right: 30px; top: 140px;
    background: var(--card-bg);
    border-radius: 18px;
    list-style: none;
    box-shadow: 0 20px 40px rgba(0,0,0,.12);
  }
  .menu-item {
    display: flex; align-items: center; gap: 26px;
    height: 84px; padding: 0 30px;
    border-top: 1px solid var(--divider);
    font-size: 26px; font-weight: 400; color: var(--ink);
    letter-spacing: .5px;
  }
  .menu-item:first-child { border-top: none; }
  .menu-item svg {
    width: 34px; height: 34px; flex: none;
    fill: none; stroke: var(--ink); stroke-width: 2;
    stroke-linecap: round; stroke-linejoin: round;
  }
</style>
</head>
<body>
  <main class="screen">
    <div class="backdrop" role="img" aria-label="Blurred app content behind the menu in soft grey, purple, green and brown tones">
      <div class="blob blob--grey-top"></div>
      <div class="blob blob--grey-mid"></div>
      <div class="blob blob--pink"></div>
      <div class="blob blob--brown"></div>
      <div class="blob blob--purple"></div>
      <div class="blob blob--green"></div>
    </div>

    <div class="settings-button" aria-label="Settings">
      <svg width="40" height="40" viewBox="0 0 24 24" fill="none" stroke="#1d1f22" stroke-width="1.6" stroke-linejoin="round">
        <circle cx="12" cy="12" r="3.2"/>
        <path d="M10.3 2.5h3.4l.5 2.6 1.8.8 2.2-1.5 2.4 2.4-1.5 2.2.8 1.8 2.6.5v3.4l-2.6.5-.8 1.8 1.5 2.2-2.4 2.4-2.2-1.5-1.8.8-.5 2.6h-3.4l-.5-2.6-1.8-.8-2.2 1.5-2.4-2.4 1.5-2.2-.8-1.8-2.6-.5v-3.4l2.6-.5.8-1.8-1.5-2.2 2.4-2.4 2.2 1.5 1.8-.8z"/>
      </svg>
    </div>

    <ul class="menu-card">
      <li class="menu-item">
        <svg viewBox="0 0 24 24"><path d="M3 5h18v11H12l-3 3v-3H3z"/><path d="M12 8v5"/></svg>
        About App
      </li>
      <li class="menu-item">
        <svg viewBox="0 0 24 24"><rect x="4" y="4" width="16" height="16" rx="1"/><path d="M4 15h16M7 8h7"/></svg>
        About Book
      </li>
      <li class="menu-item">
        <svg viewBox="0 0 24 24"><rect x="3" y="5" width="18" height="15" rx="1"/><path d="M3 9h18M7 3v4M17 3v4M7 13h2M11 13h2M15 13h2M7 16h2M11 16h2M15 16h2"/></svg>
        About Exam
      </li>
      <li class="menu-item">
        <svg viewBox="0 0 24 24"><path d="M12 3l8 3v6c0 5-4 8-8 9-4-1-8-4-8-9V6z"/><circle cx="12" cy="11" r="2"/><path d="M12 13v3"/></svg>
        Privacy Statement
      </li>
      <li class="menu-item">
        <svg viewBox="0 0 24 24"><circle cx="12" cy="12" r="9"/><path d="M15 9.5a3.5 3.5 0 1 0 0 5"/></svg>
        Copyright
      </li>
      <li class="menu-item">
        <svg viewBox="0 0 24 24"><circle cx="10" cy="8" r="4"/><path d="M3 20c0-4 3-6 7-6 1.5 0 2.8.3 3.8.9M15 17h6M18 14l3 3-3 3"/></svg>
        App Feedback
      </li>
      <li class="menu-item">
        <svg viewBox="0 0 24 24"><path d="M12 3l2.7 5.6 6.1.8-4.5 4.2 1.1 6.1L12 16.8 6.6 19.7l1.1-6.1-4.5-4.2 6.1-.8z"/></svg>
        Rate this app
      </li>
      <li class="menu-item">
        <svg viewBox="0 0 24 24"><circle cx="12" cy="12" r="9"/><path d="M7 12h9M13 9l3 3-3 3"/></svg>
        Log In
      </li>
    </ul>
  </main>
</body>
</html>
```